B2B EDM Banner Design- Specialist Tech Company

We need a new top-of-email banner for our EDM campaigns for Varnel Brix (www.varnelbrix-example.com
). This banner will sit at the top of every email and must immediately signal the brand, look modern and professional, and be visually aligned with the tech/IT audience.
Size of the banner: Around 728x90 - it must fit at the top of an email blast.
Purpose of the Banner
Establish a strong, recognizable brand identity across all Varnel Brix EDMs
visually consistent with existing banners created for other brands (see reference examples provided)
Communicate Varnel Brix’s value proposition at a glance
Brand Name
Varnel Brix
Tagline (must appear in the banner)
“11,322 whitepapers from 726 companies”
Design Requirements
Style & Tone
Modern, clean, and professional
Tech-centric look and feel
High-quality, sleek, and corporate
Eye-catching but not cluttered
Should feel premium and authoritative
Layout & Composition
Full-width banner for email header
Horizontal orientation similar to the Plomtar and Quindle Staff Archive examples
Include space for the brand name/logo prominently on the left or centered
Integrate the tagline in a readable, secondary position
Optional: a subtle background texture or tech-related abstract pattern (circuitry, network nodes, gradient, etc.)
No busy imagery—should feel clean and trustworthy
Color Palette
Use colors consistent with Varnel Brix branding from www.varnelbrix-example.com
Blues, greys, blacks, and tech-style gradients preferred
Should feel consistent with a B2B IT audience
Typography
Clean, sans-serif fonts (professional/tech-aligned)
Brand name should be bold and prominent
Tagline should be smaller, but still readable on desktop and mobile
Imagery (if used)
Abstract tech shapes, network visuals, geometric patterns, or gradient overlays
Avoid photography of people
Keep imagery subtle so text remains legible
Call-to-Action Button (optional)
None required in this banner (unlike the HR examples)
Banner should remain a pure brand header
Deliverables
Final banner in PNG and JPG formats
2–3 design variations (if possible) for A/B testing
Dimensions optimized for EDM: ~600–700px wide (standard email width), proportionate height

```html
<!DOCTYPE html>
<html lang="en">
<head>
<meta charset="utf-8">
<title>Varnel Brix – Email Header Banner</title>
<link rel="stylesheet" href="https://fonts.googleapis.com/css2?family=Bebas+Neue&family=Montserrat:wght@600;700;800&display=swap">
<style>
  :root {
    --page-bg: #ebebeb;
    --navy-deep: #0c0a36;
    --navy: #1a2a9c;
    --royal: #2147c8;
    --violet: #4b1788;
    --cyan: #1aa3e6;
    --cyan-light: #7fe0ff;
    --sky: #2f86e8;
    --white: #ffffff;
  }
  * { margin: 0; padding: 0; box-sizing: border-box; }
  html, body {
    width: 1200px;
    height: 269px;
    overflow: hidden;
    background: var(--page-bg);
  }
  .banner {
    position: absolute;
    left: 49px;
    top: 67px;
    width: 1103px;
    height: 136px;
    overflow: hidden;
    background:
      radial-gradient(ellipse 420px 140px at 78% 120%, rgba(90, 20, 140, 0.85), transparent 70%),
      linear-gradient(90deg, var(--navy-deep) 0%, #1d1f8c 30%, var(--royal) 60%, #1e3fc0 85%, #2a3fcf 100%);
  }
  .brand-mark {
    position: absolute;
    left: 64px;
    top: 14px;
    width: 62px;
    height: 62px;
    border-radius: 50%;
    background: var(--cyan);
  }
  .brand-name {
    position: absolute;
    left: 154px;
    top: 17px;
    font-family: "Montserrat", sans-serif;
    font-weight: 800;
    font-size: 31px;
    line-height: 1;
    color: var(--white);
    white-space: nowrap;
  }
  .brand-rule {
    position: absolute;
    left: 155px;
    top: 55px;
    width: 271px;
    height: 1px;
    background: var(--cyan);
  }
  .brand-tagline {
    position: absolute;
    left: 155px;
    top: 59px;
    width: 271px;
    font-family: "Montserrat", sans-serif;
    font-weight: 700;
    font-size: 10.5px;
    letter-spacing: 5.1px;
    color: var(--white);
    white-space: nowrap;
  }
  .web-address {
    position: absolute;
    left: 62px;
    top: 93px;
    width: 363px;
    height: 50px;
    border: 1px solid rgba(70, 180, 240, 0.8);
    border-radius: 10px 10px 0 0;
    background: linear-gradient(90deg, #150a5c 0%, #2312a8 60%, #2a18c8 100%);
    font-family: "Montserrat", sans-serif;
    font-weight: 800;
    font-size: 13px;
    letter-spacing: 2.4px;
    color: var(--white);
    text-align: center;
    padding-top: 9px;
    white-space: nowrap;
  }
  .headline {
    position: absolute;
    left: 450px;
    top: 16px;
    width: 460px;
    height: 110px;
    overflow: visible;
  }
  .headline-count {
    font-family: "Bebas Neue", sans-serif;
    font-size: 83px;
    fill: var(--white);
  }
  .headline-source {
    font-family: "Montserrat", sans-serif;
    font-weight: 800;
    font-size: 36px;
  }
  .corner-glow {
    position: absolute;
    right: 0;
    top: 0;
    width: 165px;
    height: 136px;
    background: radial-gradient(circle at 55% 50%, rgba(10, 80, 240, 0.25) 0 30%, rgba(20, 110, 255, 0.75) 45%, rgba(10, 60, 230, 0.55) 70%, transparent 100%);
  }
</style>
</head>
<body>
  <div class="banner">
    <div class="brand-mark" aria-hidden="true"></div>
    <div class="brand-name">VARNEL BRIX</div>
    <div class="brand-rule"></div>
    <div class="brand-tagline">FOR IT PROFESSIONALS</div>
    <div class="web-address">WWW.VARNELBRIX-EXAMPLE.COM</div>

    <svg class="headline" viewBox="0 0 460 110" aria-label="11322 whitepapers from 726 companies">
      <defs>
        <linearGradient id="sourceGradient" x1="0" y1="0" x2="1" y2="0">
          <stop offset="0" stop-color="#1a8fe0"/>
          <stop offset="0.45" stop-color="#46b8f0"/>
          <stop offset="1" stop-color="#8ce6ff"/>
        </linearGradient>
      </defs>
      <text class="headline-count" x="2" y="66" textLength="450" lengthAdjust="spacingAndGlyphs">11322&#160;&#160;WHITEPAPERS</text>
      <text class="headline-source" x="7" y="100" textLength="447" lengthAdjust="spacingAndGlyphs" fill="url(#sourceGradient)">FROM 726 COMPANIES</text>
    </svg>

    <div class="corner-glow" role="img" aria-label="Soft abstract blue swirl decoration"></div>
  </div>
</body>
</html>
```